I sell Finches---picture of White Finch Bird----

I raise and sell light color and white Finch - need card to give to Pet shops with my name - Dora Pelkey, address: 271 North Corwen St. Marlow Springs, Ca. 95872 - phone - 555-417-3968. All birds raised and nourished in large outside aviary--very healthy and cared for. Would like card to be shiny red with bold print in Broadway font----purple bold print on red card. Design options open - you know best. Would like a picture or pictures of Finches - light or white in color.

THE WREN KEEPER (LARGE, BOLD BROADWAY PRINT)

```html
<!DOCTYPE html>
<html lang="en">
<head>
<meta charset="utf-8">
<title>The Wren Keeper – Business Card</title>
<link href="https://fonts.googleapis.com/css2?family=Limelight&display=swap" rel="stylesheet">
<style>
  :root {
    --page-bg: #e9e9e9;
    --card-red: #d91f2b;
    --card-red-light: #e2394a;
    --ink-purple: #6e2166;
    --title-white: #ffffff;
    --photo-dark: #3b2a12;
    --photo-mid: #7a5a24;
    --photo-gold: #b99a3e;
    --photo-white: #f3f1ea;
  }
  * { margin: 0; padding: 0; box-sizing: border-box; }
  html, body {
    width: 1200px;
    height: 1000px;
    overflow: hidden;
    background: var(--page-bg);
  }
  .stage {
    width: 1200px;
    height: 1000px;
    display: flex;
    flex-direction: column;
    align-items: center;
    justify-content: center;
    gap: 50px;
  }
  .card {
    width: 720px;
    height: 411px;
    position: relative;
    overflow: hidden;
    box-shadow: 0 6px 18px rgba(0,0,0,0.25);
  }
  /* Front */
  .card-front__photo {
    position: absolute;
    inset: 0;
    background:
      radial-gradient(ellipse 48% 40% at 62% 62%, var(--photo-white) 0%, rgba(243,241,234,0.85) 45%, rgba(243,241,234,0) 100%),
      radial-gradient(ellipse 40% 30% at 80% 30%, rgba(243,241,234,0.7) 0%, rgba(243,241,234,0) 100%),
      radial-gradient(ellipse 70% 60% at 85% 80%, var(--photo-gold) 0%, rgba(185,154,62,0) 70%),
      linear-gradient(135deg, var(--photo-mid) 0%, var(--photo-dark) 55%, var(--photo-mid) 100%);
  }
  .card-front__title {
    position: absolute;
    left: 40px;
    top: 36px;
    font-family: "Limelight", serif;
    font-weight: 400;
    font-size: 56px;
    color: var(--title-white);
    letter-spacing: 1px;
    white-space: nowrap;
  }
  /* Back */
  .card-back {
    background: linear-gradient(160deg, var(--card-red-light) 0%, var(--card-red) 45%, var(--card-red) 100%);
    color: var(--ink-purple);
    font-family: "Limelight", serif;
    text-align: center;
    display: flex;
    flex-direction: column;
    align-items: center;
    padding: 34px 24px 0;
  }
  .card-back__title {
    font-size: 58px;
    font-weight: 400;
    line-height: 1;
    letter-spacing: 1px;
    white-space: nowrap;
  }
  .card-back__name {
    margin-top: 26px;
    font-size: 30px;
  }
  .card-back__phone {
    margin-top: 20px;
    font-size: 21px;
  }
  .card-back__address {
    margin-top: 6px;
    font-size: 21px;
    line-height: 1.3;
  }
  .card-back__tagline {
    margin-top: 20px;
    font-size: 19px;
    line-height: 1.3;
  }
</style>
</head>
<body>
<main class="stage">
  <section class="card card-front">
    <div class="card-front__photo" role="img" aria-label="Photograph of white finches perched on white water lilies in a golden bird bath"></div>
    <h1 class="card-front__title">THE WREN KEEPER</h1>
  </section>
  <section class="card card-back">
    <h2 class="card-back__title">THE WREN KEEPER</h2>
    <p class="card-back__name">Dora Pelkey</p>
    <p class="card-back__phone">Phone - 555-417-3968</p>
    <p class="card-back__address">Address: 271 North Corwen St. Marlow Springs,<br>CA. 95872</p>
    <p class="card-back__tagline">All birds raised and nourished in large outside aviary.<br>Very healthy and cared for</p>
  </section>
</main>
</body>
</html>
```